Corvella Website Homepage

Committed to delivering quality content, quillpagewords.com is a content providing company. Equipped with resourceful writers with industry experience, we promise to empower our clients with content that is tailor-made to address specific requirements of their target Audience.

We need a website home page and one internal page designed. It is very important that the page be laid out with SEO in mind. We like the idea of using five images as navigation to our services. The five major services we offer are:
• Web Content writing (articles, features, website copy etc)
• Business Content writing (Press release, mailers & flyers, brochure/catalog)
• Personal Content writing (blog, speech writing)
• Hire a writer/editor
• Proof reading and editing services
The sample template (http://pv7.layoutdemo-hub.net/dx_48270/index.html) included has five images in the first fold. Designer can choose the right image for each service and lay over the service name on the image. Please do not use flash ( We will use javascripts). We need to have a detailed right side nav as in the template for SEO reasons. There will be some marketing ad- copy below the main images. Followed by a 200 character SEO optimized text defining our services in further detail. Apart from these a designer is free to use his creativity. The name of the site will be http://www.quillpagewords.com/. This name will need a logo too. Please include it as part of design. Corvellacorp is the owner of quillpagewords.com. We already have a logo for Corvella that is attached here as a separate file.

We have some taglines that need to be incorporated in the home page and other pages.
Please provide link button for Home, About us, Services, Samples, Pricing, Clients, Career, Contact us.

Links can be given on TOP, Sideways and Bottom and in the drop down menu of services etc.

Reason: Hi

We have made our project guaranteed and extended deadline by 5 days so you get more time to complete our project.

Thanks and Regards,

Ravindra Kulkarni
Corvellacorp

Target Market(s)

Product Marketing Companies - Mostly in US.
Media companies which publish articles on various subjects. Travel and Lifestyle related sites, Educational Websites, Government Websites, Health related websites,

Industry/Entity Type

Marketing

Requirements
Must have
• Color of Homepage should blend with sober mood of the content. Writing Services should get highlighted in such a way that any person serious about the business visiting the site get attracted to read on the details of our content services. Most space should be used for details of writing services and links for our various pages and services. Webpage should be downloaded in lowest possible time.
Nice to have
• We have some idea about the website layouts;-http://www.skinbazaarly.net/site-layouts/48270.html - layout of information http://www.skinbazaarly.net/site-layouts/47359.html - for kind of marketing http://pv7.layoutdemo-hub.net/dx_48615/index.html - for colors
we attach a word file representing our idea in some way but not limited to it.
Should not have
• Gaudy (aggressive dark) colors. It should not be cluttered. No flash.

```html
<!DOCTYPE html>
<html lang="en">
<head>
<meta charset="utf-8">
<title>Quillpage Words – Content Writing Services</title>
<link href="https://fonts.googleapis.com/css2?family=Arimo:wght@400;700&family=Roboto+Condensed:wght@700&display=swap" rel="stylesheet">
<style>
:root{
  --strip:#a8e090;
  --dark-top:#0f0f0f;
  --dark-bottom:#3b3b3b;
  --red:#c22f3b;
  --blue:#1b76a0;
  --green-title:#2b7412;
  --green-head:#4a8f2c;
  --green-box:#cdf9c8;
  --green-line:#9ccf96;
  --blue-box:#cdeefc;
  --link:#1c4f80;
  --text:#111;
  --footer:#333;
  --copy:#b6e66a;
  --side-line:#d8d8d8;
}
*{margin:0;padding:0;box-sizing:border-box}
html,body{width:1200px;height:1001px;overflow:hidden}
body{position:relative;background:#fff;font-family:Arimo,Arial,sans-serif;color:var(--text)}
a{color:inherit;text-decoration:none}
.abs{position:absolute}

.top-strip{left:0;top:0;width:1200px;height:9px;background:var(--strip)}
.header{left:0;top:9px;width:1200px;height:431px;background:linear-gradient(var(--dark-top),var(--dark-bottom))}

.brand{left:105px;top:34px;display:flex;align-items:center;gap:10px;color:#fff;font-size:24px;font-weight:400;letter-spacing:.5px;white-space:nowrap}
.brand-dot{width:46px;height:46px;border-radius:50%;background:var(--blue)}

.main-nav{top:44px;left:428px;height:28px}
.main-nav a{position:absolute;top:0;height:28px;line-height:28px;color:#fff;font-weight:700;font-size:12px;white-space:nowrap}
.main-nav a.active{background:var(--red);border-radius:4px;padding:0 11px}

.stage{left:104px;top:100px;width:996px;height:340px;background:#fff;border-radius:8px 8px 0 0}
.tagline{left:119px;top:132px;font-size:22.5px;font-weight:400;color:#333;white-space:nowrap}
.tagline strong{font-weight:400;color:var(--green-head)}
.partner{left:910px;top:112px;width:175px;height:66px;display:flex;align-items:center;justify-content:flex-end;color:var(--red);font-size:28px;font-weight:700}

.service-tile{top:189px;width:179px;height:249px}
.service-photo{height:209px;background:linear-gradient(160deg,#e4e4e4,#8a8a8a 60%,#555)}
.service-label{height:40px;line-height:42px;text-align:center;color:#fff;font-family:'Roboto Condensed',Arial,sans-serif;font-weight:700;font-size:13px;white-space:nowrap}
.red{background:var(--red)}.blue{background:var(--blue)}

.intro-title{left:121px;top:464px;font-family:'Roboto Condensed',sans-serif;font-size:18px;color:var(--red)}
.intro-text{left:122px;top:496px;width:702px;font-size:14px;line-height:18px;text-align:justify}

.panel{top:588px;width:340px;height:298px}
.usp{left:119px;background:var(--green-box)}
.direct{left:484px;background:var(--blue-box)}
.panel h2{position:absolute;left:7px;top:11px;font-size:20px;font-weight:700}
.usp h2{color:var(--green-title)}
.direct h2{left:11px;color:var(--blue)}
.panel .lead{position:absolute;font-size:12.5px;font-weight:700;line-height:16px}
.usp .lead{left:9px;top:44px;width:325px}
.direct .lead{left:12px;top:40px;width:307px;text-align:justify}

.usp ul{position:absolute;left:8px;top:82px;width:321px;list-style:none}
.usp li{height:30px;display:flex;align-items:center;font-size:12px;border-bottom:1px solid var(--green-line)}
.usp li:last-child{border-bottom:0}
.usp li svg{flex:none;width:24px;height:22px;margin-right:11px}
.usp li span{padding-top:2px}

.ad-image{position:absolute;left:13px;top:79px;width:307px;height:86px;background:linear-gradient(90deg,#3a1410,#8a3a20 35%,#c24a3a 65%,#3a1a20)}
.direct ul{position:absolute;left:12px;top:170px;list-style:none}
.direct li{height:20px;font-size:12px;color:#222}
.direct li::before{content:"››";color:var(--red);font-weight:700;margin-right:5px}

.sidebar{left:848px;top:462px;width:238px;height:427px;border:1px solid #ddd;border-radius:6px;overflow:hidden}
.sidebar h3{height:36px;line-height:36px;background:#1f1f1f;color:#fff;font-weight:400;font-size:20px;padding-left:12px}
.sidebar ul{list-style:none;margin-top:4px}
.sidebar li{height:28px;display:flex;align-items:center;margin:0 10px 0 12px;font-size:12px;color:var(--link);position:relative}
.sidebar li::after{content:"";position:absolute;left:16px;right:0;bottom:0;border-bottom:1px solid var(--side-line)}
.sidebar li svg{width:12px;height:12px;margin-right:8px}

.footer{left:0;top:920px;width:1200px;height:81px;background:var(--footer)}
.footer-nav a{position:absolute;top:955px;color:#fff;font-size:11px}
.copyright{right:116px;top:955px;font-size:11px;color:var(--copy)}
</style>
</head>
<body>
<div class="abs top-strip"></div>
<header class="abs header"></header>

<a class="abs brand" href="#"><span class="brand-dot"></span>QUILLPAGE WORDS</a>

<nav class="abs main-nav">
  <a class="active" href="#" style="left:0">HOME</a>
  <a href="#" style="left:72px">ABOUT US</a>
  <a href="#" style="left:164px">SERVICES</a>
  <a href="#" style="left:253px">SAMPLES</a>
  <a href="#" style="left:342px">PRICING</a>
  <a href="#" style="left:421px">CLIENTS</a>
  <a href="#" style="left:502px">CAREER</a>
  <a href="#" style="left:581px">CONTACT US</a>
</nav>

<section class="abs stage"></section>
<h1 class="abs tagline"><strong>CRAS TRISTIQUE AUGUE NON</strong> elit elementum aliquam</h1>
<div class="abs partner">Corvella</div>

<a class="abs service-tile" href="#" style="left:120px"><div class="service-photo" role="img" aria-label="Hands working at a laptop with documents"></div><div class="service-label red">WEB CONTENT WRITING</div></a>
<a class="abs service-tile" href="#" style="left:316px"><div class="service-photo" role="img" aria-label="Business team meeting at a table"></div><div class="service-label blue">BUSINESS CONTENT WRITING</div></a>
<a class="abs service-tile" href="#" style="left:513px"><div class="service-photo" role="img" aria-label="Handwritten letter with a quill pen"></div><div class="service-label red">PERSONAL CONTENT WRITING</div></a>
<a class="abs service-tile" href="#" style="left:709px"><div class="service-photo" role="img" aria-label="Writers and editors reviewing papers together"></div><div class="service-label blue">HIRE A WRITER / EDITOR</div></a>
<a class="abs service-tile" href="#" style="left:905px"><div class="service-photo" role="img" aria-label="Two people proofreading a document"></div><div class="service-label red">PROOF READING &amp; EDITING</div></a>

<h2 class="abs intro-title">LOREM IPSUM DOLAR SIT AMET</h2>
<p class="abs intro-text">Consectetur adipiscing elit. Duis viverra, risus eget porta pretium, felis leo suscipit eros, vel sollicitudin elit turpis ac turpis. Mauris sed quam turpis. Etiam et augue nisl, nec viverra lacus. Nam pharetra leo in magna gravida id mollis lorem cursus. Fusce eu tellus leo, nec pharetra orci. Integer nec tortor nisl, eget lacinia nulla. Vivamus sagittis urna vitae massa fermentum posuere.</p>

<section class="abs panel usp">
  <h2>USPs for Marketing</h2>
  <p class="lead">Why choose Quillpagewords.com to “e - SOURCE” your content:</p>
  <ul>
    <li><svg viewBox="0 0 24 22"><rect x="1" y="4" width="22" height="14" fill="#2a3f8a"/><path d="M1 4L23 18M23 4L1 18" stroke="#fff" stroke-width="3"/><path d="M12 4v14M1 11h22" stroke="#fff" stroke-width="4"/><path d="M12 4v14M1 11h22" stroke="#c22" stroke-width="2"/></svg><span><b>ENGLISH</b> American and British.</span></li>
    <li><svg viewBox="0 0 24 22"><path d="M2 18V8l18-6v16z" fill="#5cbf4a"/><path d="M2 18h18" stroke="#2b7a1a" stroke-width="2"/></svg><span><b>SUCCESS</b> stories of our clients</span></li>
    <li><svg viewBox="0 0 24 22"><circle cx="10" cy="9" r="7" fill="#bfe6ff" stroke="#1a86d0" stroke-width="2.5"/><path d="M15 14l6 6" stroke="#1a5fa0" stroke-width="3.5" stroke-linecap="round"/></svg><span><b>OPTIMIZED</b> content for Search Engines</span></li>
    <li><svg viewBox="0 0 24 22"><rect x="2" y="3" width="18" height="15" rx="2" fill="#4a7fd0"/><path d="M6 18l6-12 6 12" fill="#f0c030"/></svg><span><b>ULTRA</b> high speed delivery</span></li>
    <li><svg viewBox="0 0 24 22"><path d="M3 17L8 3h13l-5 14z" fill="#3a4a66"/><path d="M3 17h13l5-14" fill="none" stroke="#9aa" stroke-width="1.5"/></svg><span>Intensive <b>RESEARCH</b></span></li>
    <li><svg viewBox="0 0 24 22"><circle cx="11" cy="11" r="9" fill="#ee7a22"/><text x="11" y="16" text-anchor="middle" font-family="Arimo,sans-serif" font-size="13" font-weight="700" fill="#fff">$</text></svg><span>Competitive <b>COST</b></span></li>
    <li><svg viewBox="0 0 24 22"><path d="M4 11h4v9H4zM9 11l4-8c2 0 2 2 2 4h5c2 0 2 3 1 4l-2 8H9z" fill="#f29a2e"/></svg><span>Team of subject matter <b>EXPERTS</b></span></li>
  </ul>
</section>

<section class="abs panel direct">
  <h2>Direct Marketing</h2>
  <p class="lead">Praesent nisi nibh, semper sit amet dapibus quis, dictum ut ligula. Proin imperdiet posuere nulla:</p>
  <div class="ad-image" role="img" aria-label="Word cloud of web marketing and search terms"></div>
  <ul>
    <li>Aliquam hendrerit egestas libero, ac varius tortor</li>
    <li>Fusce sagittis felis id erat pharetra</li>
    <li>Cras scelerisque vehicula quam, sed mollis</li>
    <li>Morbi id risus vel metus iaculis aliquet id ut eros.</li>
    <li>In ultrices quam ac lacus faucibus vitae</li>
    <li>Fusce suscipit diam quis</li>
  </ul>
</section>

<aside class="abs sidebar">
  <h3>Our Services</h3>
  <ul>
    <li><svg viewBox="0 0 12 12"><circle cx="6" cy="6" r="5.3" fill="#fff" stroke="#999"/><path d="M5 3.5L7.5 6 5 8.5" fill="none" stroke="#555" stroke-width="1.3"/></svg>Lorem</li>
    <li><svg viewBox="0 0 12 12"><circle cx="6" cy="6" r="5.3" fill="#fff" stroke="#999"/><path d="M5 3.5L7.5 6 5 8.5" fill="none" stroke="#555" stroke-width="1.3"/></svg>Ut in erat</li>
    <li><svg viewBox="0 0 12 12"><circle cx="6" cy="6" r="5.3" fill="#fff" stroke="#999"/><path d="M5 3.5L7.5 6 5 8.5" fill="none" stroke="#555" stroke-width="1.3"/></svg>Sed egestas</li>
    <li><svg viewBox="0 0 12 12"><circle cx="6" cy="6" r="5.3" fill="#fff" stroke="#999"/><path d="M5 3.5L7.5 6 5 8.5" fill="none" stroke="#555" stroke-width="1.3"/></svg>Duis eget lectus</li>
    <li><svg viewBox="0 0 12 12"><circle cx="6" cy="6" r="5.3" fill="#fff" stroke="#999"/><path d="M5 3.5L7.5 6 5 8.5" fill="none" stroke="#555" stroke-width="1.3"/></svg>Quisque tempus</li>
    <li><svg viewBox="0 0 12 12"><circle cx="6" cy="6" r="5.3" fill="#fff" stroke="#999"/><path d="M5 3.5L7.5 6 5 8.5" fill="none" stroke="#555" stroke-width="1.3"/></svg>Phasellus</li>
    <li><svg viewBox="0 0 12 12"><circle cx="6" cy="6" r="5.3" fill="#fff" stroke="#999"/><path d="M5 3.5L7.5 6 5 8.5" fill="none" stroke="#555" stroke-width="1.3"/></svg>Suspendisse</li>
    <li><svg viewBox="0 0 12 12"><circle cx="6" cy="6" r="5.3" fill="#fff" stroke="#999"/><path d="M5 3.5L7.5 6 5 8.5" fill="none" stroke="#555" stroke-width="1.3"/></svg>Aliquam hendrerit</li>
    <li><svg viewBox="0 0 12 12"><circle cx="6" cy="6" r="5.3" fill="#fff" stroke="#999"/><path d="M5 3.5L7.5 6 5 8.5" fill="none" stroke="#555" stroke-width="1.3"/></svg>Fusce sagittis</li>
    <li><svg viewBox="0 0 12 12"><circle cx="6" cy="6" r="5.3" fill="#fff" stroke="#999"/><path d="M5 3.5L7.5 6 5 8.5" fill="none" stroke="#555" stroke-width="1.3"/></svg>Cras scelerisque</li>
    <li><svg viewBox="0 0 12 12"><circle cx="6" cy="6" r="5.3" fill="#fff" stroke="#999"/><path d="M5 3.5L7.5 6 5 8.5" fill="none" stroke="#555" stroke-width="1.3"/></svg>Morbi id risus</li>
    <li><svg viewBox="0 0 12 12"><circle cx="6" cy="6" r="5.3" fill="#fff" stroke="#999"/><path d="M5 3.5L7.5 6 5 8.5" fill="none" stroke="#555" stroke-width="1.3"/></svg>In ultrices</li>
    <li><svg viewBox="0 0 12 12"><circle cx="6" cy="6" r="5.3" fill="#fff" stroke="#999"/><path d="M5 3.5L7.5 6 5 8.5" fill="none" stroke="#555" stroke-width="1.3"/></svg>Fusce</li>
  </ul>
</aside>

<footer class="abs footer"></footer>
<nav class="footer-nav">
  <a href="#" style="left:118px">HOME</a>
  <a href="#" style="left:174px">ABOUT US</a>
  <a href="#" style="left:259px">SERVICES</a>
  <a href="#" style="left:342px">SAMPLES</a>
  <a href="#" style="left:423px">PRICING</a>
  <a href="#" style="left:495px">CLIENTS</a>
  <a href="#" style="left:569px">CAREER</a>
  <a href="#" style="left:643px">CONTACT US</a>
</nav>
<p class="abs copyright">Copyright © 2011 Quillpagewords.com</p>
</body>
</html>
```